We are an appraisal and dispute resolution company that works with insurance companies and insureds.

We need a website built that appeals to insurance companies as well as insureds to entrust we can assist come to a resolution with their property insurance claim.

Target Market(s)

Insurance Carriers and Insureds

Industry/Entity Type

Insurance

Coding

Coded - Design and coding required

Number of Pages Required

5+ page

Requirements
Must have
• Would like to click on pages and it take you down one page to that specific section
Nice to have
• Clean look

```html
<!DOCTYPE html>
<html lang="en">
<head>
<meta charset="utf-8">
<title>VALRO – Valley Appraisal and Resolution Office</title>
<link href="https://fonts.googleapis.com/css2?family=Poppins:wght@400;500;600;700&family=Roboto:wght@400;500&display=swap" rel="stylesheet">
<style>
:root{
  --teal:#3cc4c8;
  --teal-soft:#e4f6f6;
  --navy:#1f2333;
  --ink:#222633;
  --body:#3b3f4a;
  --line:#cfd3d8;
  --white:#ffffff;
}
*{box-sizing:border-box;margin:0;padding:0}
html,body{width:1200px;height:4102px;overflow:hidden}
body{position:relative;background:var(--white);font-family:"Roboto",Arial,sans-serif;color:var(--body)}
.abs{position:absolute}
h2.section-title{position:absolute;left:0;width:1200px;text-align:center;font-family:"Poppins",sans-serif;font-weight:600;font-size:34px;color:var(--ink)}
h2 span,.split-title span{color:var(--teal)}
.btn{position:absolute;display:flex;align-items:center;justify-content:center;font-family:"Roboto",sans-serif;font-size:13px;color:var(--white);background:var(--teal);border-radius:3px;text-decoration:none;letter-spacing:.3px}

/* header */
.site-header{position:absolute;left:0;top:0;width:1200px;height:67px;z-index:5;border-bottom:1px solid rgba(255,255,255,.25)}
.brand{position:absolute;left:111px;top:4px;color:var(--white);font-family:"Poppins",sans-serif}
.brand-name{font-size:46px;font-weight:700;line-height:48px;letter-spacing:1px}
.brand-sub{font-size:8px;font-weight:600;letter-spacing:.2px}
.main-nav a{position:absolute;top:24px;font-family:"Roboto",sans-serif;font-size:13px;color:var(--white);text-decoration:none}
.main-nav a.active{color:var(--teal)}
.main-nav a.active::after{content:"";position:absolute;left:-4px;right:-4px;top:40px;height:2px;background:var(--teal)}
.nav-cta{position:absolute;left:994px;top:18px;width:93px;height:35px;border:1px solid var(--white);border-radius:3px;color:var(--white);font-size:13px;display:flex;align-items:center;justify-content:center}

/* hero */
.hero-photo{position:absolute;left:0;top:0;width:1200px;height:730px}
.hero-box{position:absolute;left:111px;top:220px;width:546px;height:210px;background:rgba(40,44,58,.35)}
.hero-title{position:absolute;left:156px;top:228px;font-family:"Poppins",sans-serif;font-weight:600;font-size:78px;color:var(--white);line-height:1}
.hero-text{position:absolute;left:156px;top:316px;width:480px;font-size:15px;line-height:24px;color:var(--white);font-weight:500}
.hero-outline{position:absolute;left:288px;top:385px;width:115px;height:33px;border:1px solid var(--white);border-radius:3px;color:var(--white);font-size:13px;display:flex;align-items:center;justify-content:center}
.slider-arrow{position:absolute;top:279px;width:72px;height:72px;border-radius:50%;border:1px solid rgba(255,255,255,.7)}
.slider-dots{position:absolute;left:572px;top:656px;display:flex;gap:6px}
.slider-dots i{width:10px;height:10px;border-radius:50%;border:1px solid var(--white)}
.slider-dots i:first-child{background:var(--white)}

/* about */
.about-text{position:absolute;left:150px;top:866px;width:900px;text-align:center;font-size:15px;line-height:30px}
.divider{position:absolute;left:111px;top:1021px;width:977px;height:1px;background:var(--line)}
.divider-knob{position:absolute;left:579px;top:1002px;width:38px;height:38px;border-radius:50%;background:var(--teal);box-shadow:0 0 0 5px #d9f3f3}

/* split features */
.split-title{position:absolute;font-family:"Poppins",sans-serif;font-weight:600;font-size:35px;color:var(--ink)}
.split-text{position:absolute;width:410px;font-size:14.5px;line-height:25px}
.round-photo{position:absolute;border-radius:50%}

/* services */
.service-card{position:absolute;width:220px;height:257px;background:var(--white);border-radius:4px;text-align:center;box-shadow:0 4px 14px rgba(0,0,0,.08)}
.service-icon{position:absolute;left:65px;top:19px;width:90px;height:90px;border-radius:50%;background:var(--white);box-shadow:0 2px 10px rgba(0,0,0,.12);display:flex;align-items:center;justify-content:center}
.service-icon::before{content:"";position:absolute;inset:8px;border-radius:50%;border:1px solid var(--teal)}
.service-title{position:absolute;left:0;top:124px;width:220px;font-family:"Poppins",sans-serif;font-size:19px;font-weight:500;color:var(--ink)}
.service-text{position:absolute;left:10px;top:158px;width:200px;font-size:11.5px;line-height:19px;color:var(--body)}
.service-link{position:absolute;left:0;top:222px;width:220px;font-family:"Poppins",sans-serif;font-size:14px;font-weight:500;color:var(--teal);text-decoration:underline}

/* contact */
.contact-text{position:absolute;left:250px;top:3073px;width:700px;text-align:center;font-size:15px;line-height:25px}
.field{position:absolute;border:1px solid #d4d8dc;font-size:13px;color:#6b6f78;padding:12px 14px}

/* footer */
.footer-brand{position:absolute;left:132px;top:3792px;color:var(--white);font-family:"Poppins",sans-serif}
.footer-brand .brand-name{font-size:54px;line-height:58px}
.footer-brand .brand-sub{font-size:9.5px}
.social{position:absolute;top:3921px;width:36px;height:36px;border-radius:50%;border:1px solid rgba(255,255,255,.7)}
.footer-head{position:absolute;top:3778px;font-family:"Poppins",sans-serif;font-size:19px;font-weight:500;color:var(--white)}
.footer-links{position:absolute;top:3835px;list-style:none}
.footer-links li{font-size:11px;line-height:27px;color:var(--white);font-weight:500;text-transform:uppercase}
.contact-icon{position:absolute;left:845px;width:36px;height:36px;border-radius:50%;border:1px solid rgba(255,255,255,.7);display:flex;align-items:center;justify-content:center}
.contact-line{position:absolute;left:899px;font-size:13px;line-height:25px;color:var(--white)}
.to-top{position:absolute;left:1105px;top:3922px;width:42px;height:42px;border-radius:50%;background:var(--teal);display:flex;align-items:center;justify-content:center}
.footer-rule{position:absolute;left:111px;top:4025px;width:977px;height:1px;background:rgba(255,255,255,.25)}
.footer-bottom{position:absolute;top:4045px;font-size:12.5px;color:var(--white)}
</style>
</head>
<body>

<!-- ===== Hero ===== -->
<section id="home">
  <svg class="hero-photo" viewBox="0 0 1200 730" width="1200" height="730" role="img" aria-label="Photo of business colleagues smiling and reviewing a tablet together at a desk">
    <defs>
      <linearGradient id="heroTone" x1="0" y1="0" x2="1" y2="1">
        <stop offset="0" stop-color="#5a5f6b"/>
        <stop offset=".45" stop-color="#8b8276"/>
        <stop offset="1" stop-color="#3e4350"/>
      </linearGradient>
    </defs>
    <path d="M0 0H1200V560C1080 640 940 680 780 690C560 700 300 660 0 625Z" fill="url(#heroTone)"/>
    <path d="M0 625C300 660 560 700 780 690C940 680 1080 640 1200 560V610C1080 680 940 720 780 728C560 738 300 700 0 650Z" fill="var(--teal)"/>
  </svg>

  <header class="site-header">
    <div class="brand">
      <div class="brand-name">VALRO</div>
      <div class="brand-sub">VALLEY APPRAISAL AND RESOLUTION OFFICE</div>
    </div>
    <nav class="main-nav">
      <a class="active" href="#home" style="left:527px">Home</a>
      <a href="#about" style="left:600px">About Us</a>
      <a href="#what-we-do" style="left:694px">What we do</a>
      <a href="#how-we-work" style="left:803px">How we work</a>
      <a href="#client" style="left:923px">Client</a>
    </nav>
    <a class="nav-cta" href="#contact">Contact Us</a>
  </header>

  <div class="hero-box"></div>
  <h1 class="hero-title">VALRO</h1>
  <p class="hero-text">Perspiciatis unde omnis iste natus error sit voluptatem accusa ntium doloremque laudantium, totam rem aperiam.</p>
  <a class="btn" href="#about" style="left:156px;top:385px;width:116px;height:33px">Get Started</a>
  <a class="hero-outline" href="#contact">Contact Us</a>

  <div class="slider-arrow" style="left:20px">
    <svg width="72" height="72" viewBox="0 0 72 72"><path d="M40 26L30 36L40 46" fill="none" stroke="#fff" stroke-width="3"/></svg>
  </div>
  <div class="slider-arrow" style="left:1113px">
    <svg width="72" height="72" viewBox="0 0 72 72"><path d="M32 26L42 36L32 46" fill="none" stroke="#fff" stroke-width="3"/></svg>
  </div>
  <div class="slider-dots"><i></i><i></i><i></i><i></i></div>
</section>

<!-- ===== About ===== -->
<section id="about">
  <h2 class="section-title" style="top:812px">About <span>Us</span></h2>
  <p class="about-text">Perspiciatis unde omnis iste natus error sit voluptatem accusantium doloremque laudantium, totam rem aperiam, eaque ipsa quae ab illo inventore veritatis et quasi architecto beatae vitae dicta sunt explicabo. Nemo enim ipsam voluptatem quia voluptas sit aspernat</p>
  <div class="divider"></div>
  <div class="divider-knob">
    <svg width="38" height="38" viewBox="0 0 38 38"><path d="M13 16L19 22L25 16" fill="none" stroke="#fff" stroke-width="2.5"/></svg>
  </div>
</section>

<!-- decorative curves -->
<svg class="abs" style="left:0;top:1060px" width="1200" height="960" viewBox="0 0 1200 960">
  <path d="M1200 270C1130 280 1110 360 1125 410C1140 470 1180 520 1200 570Z" fill="var(--teal-soft)"/>
  <path d="M460 420C520 560 620 630 720 660" fill="none" stroke="#bfe9ea" stroke-width="2"/>
  <circle cx="331" cy="230" r="205" fill="none" stroke="#c8eeee" stroke-width="2"/>
  <circle cx="322" cy="240" r="198" fill="#eef9f9"/>
  <circle cx="854" cy="735" r="196" fill="none" stroke="#c8eeee" stroke-width="2"/>
  <circle cx="846" cy="745" r="190" fill="#eef9f9"/>
</svg>

<!-- ===== What we do ===== -->
<section id="what-we-do">
  <svg class="round-photo" style="left:148px;top:1112px" width="382" height="382" viewBox="0 0 382 382" role="img" aria-label="Photo of two colleagues reviewing work together at a laptop in an office">
    <defs><linearGradient id="wwdTone" x1="0" y1="0" x2="1" y2="1"><stop offset="0" stop-color="#9aa3ad"/><stop offset="1" stop-color="#d9dadb"/></linearGradient></defs>
    <circle cx="191" cy="191" r="191" fill="url(#wwdTone)"/>
  </svg>
  <h2 class="split-title" style="left:614px;top:1110px">What We <span>Do</span></h2>
  <p class="split-text" style="left:614px;top:1167px">Perspiciatis unde omnis iste natus error sit voluptatem accusantium doloremque laudantium, totam rem aperiam, eaque ipsa quae ab illo inventore veritatis et quasi architecto beatae vitae dicta sunt explicabo. oluptatem quia voluptas sit aspernatur aut odit aut fugit, sed quia consequuntur magni dolores eosqui ratione voluptatem sequi nesciunt. Neque porro quisquam.</p>
  <a class="btn" href="#what-we-do" style="left:614px;top:1388px;width:117px;height:34px">LEARN MORE</a>
</section>

<!-- ===== How we work ===== -->
<section id="how-we-work">
  <h2 class="split-title" style="left:132px;top:1622px">How We <span>Work</span></h2>
  <p class="split-text" style="left:132px;top:1680px">Perspiciatis unde omnis iste natus error sit voluptatem accusantium doloremque laudantium, totam rem aperiam, eaque ipsa quae ab illo inventore veritatis et quasi architecto beatae vitae dicta sunt explicabo. oluptatem quia voluptas sit aspernatur aut odit aut fugit, sed quia consequuntur magni dolores eosqui ratione voluptatem sequi nesciunt. Neque porro quisquam.</p>
  <a class="btn" href="#how-we-work" style="left:132px;top:1901px;width:116px;height:34px">LEARN MORE</a>
  <svg class="round-photo" style="left:672px;top:1612px" width="366" height="366" viewBox="0 0 366 366" role="img" aria-label="Photo of a team meeting around a laptop in a bright office">
    <defs><linearGradient id="hwwTone" x1="0" y1="0" x2="1" y2="1"><stop offset="0" stop-color="#c9ccce"/><stop offset="1" stop-color="#6e6a66"/></linearGradient></defs>
    <circle cx="183" cy="183" r="183" fill="url(#hwwTone)"/>
  </svg>
</section>

<!-- ===== Services ===== -->
<section id="client">
  <svg class="abs" style="left:0;top:2040px" width="1200" height="880" viewBox="0 0 1200 880" role="img" aria-label="Teal tinted background photo of people working at laptops">
    <defs><linearGradient id="svcTone" x1="0" y1="0" x2="0" y2="1"><stop offset="0" stop-color="#34b9bd"/><stop offset="1" stop-color="#43c7ca"/></linearGradient></defs>
    <path d="M0 30C80 0 200 8 420 60C620 105 800 100 1000 60C1100 40 1160 30 1200 28V808C1100 810 980 820 800 855C620 890 420 860 200 830C100 818 40 830 0 845Z" fill="url(#svcTone)"/>
  </svg>

  <!-- row 1 -->
  <div class="service-card" style="left:111px;top:2213px">
    <div class="service-icon"><svg width="40" height="40" viewBox="0 0 40 40" fill="none" stroke="#333" stroke-width="1.6"><rect x="6" y="12" width="16" height="18" rx="2"/><path d="M24 8h10v10H24z M10 18h8 M10 23h8"/></svg></div>
    <div class="service-title">Sagnido Loreseos</div>
    <p class="service-text">Perspiciatis unde omnis iste natus error sit volu ptatem accusa ntium dolor emque laudan tiumsequi</p>
    <a class="service-link">Read More</a>
  </div>
  <div class="service-card" style="left:363px;top:2213px">
    <div class="service-icon"><svg width="40" height="40" viewBox="0 0 40 40" fill="none" stroke="#333" stroke-width="1.6"><path d="M8 18v6h5l12 7V11L13 18z M13 24l2 8h4l-2-8 M30 14l4-3 M30 21h5 M30 28l4 3"/></svg></div>
    <div class="service-title">Commo doconse</div>
    <p class="service-text">Perspiciatis unde omnis iste natus error sit volu ptatem accusa ntium dolor emque laudan tiumsequi</p>
    <a class="service-link">Read More</a>
  </div>
  <div class="service-card" style="left:614px;top:2213px">
    <div class="service-icon"><svg width="40" height="40" viewBox="0 0 40 40" fill="none" stroke="#333" stroke-width="1.6"><rect x="6" y="6" width="28" height="28" rx="8"/><circle cx="14" cy="15" r="3"/><circle cx="26" cy="15" r="3"/><circle cx="14" cy="26" r="3"/><circle cx="26" cy="26" r="3"/></svg></div>
    <div class="service-title">Qauteir Uredolor</div>
    <p class="service-text">Perspiciatis unde omnis iste natus error sit volu ptatem accusa ntium dolor emque laudan tiumsequi</p>
    <a class="service-link">Read More</a>
  </div>
  <div class="service-card" style="left:866px;top:2213px">
    <div class="service-icon"><svg width="40" height="40" viewBox="0 0 40 40" fill="none" stroke="#333" stroke-width="1.6"><circle cx="20" cy="21" r="14"/><circle cx="20" cy="21" r="9"/><circle cx="20" cy="21" r="4"/><path d="M20 21L33 8 M29 8h4v4"/></svg></div>
    <div class="service-title">Laborisnisi utliquip</div>
    <p class="service-text">Perspiciatis unde omnis iste natus error sit volu ptatem accusa ntium dolor emque laudan tiumsequi</p>
    <a class="service-link">Read More</a>
  </div>

  <!-- row 2 -->
  <div class="service-card" style="left:111px;top:2509px">
    <div class="service-icon"><svg width="40" height="40" viewBox="0 0 40 40" fill="none" stroke="#333" stroke-width="1.6"><path d="M5 33h30 M9 33V25h5v8 M17 33V19h5v14 M25 33V13h5v20 M8 20l8-6 6 3 10-9"/></svg></div>
    <div class="service-title">Sagnido Loreseos</div>
    <p class="service-text">Perspiciatis unde omnis iste natus error sit volu ptatem accusa ntium dolor emque laudan tiumsequi</p>
    <a class="service-link">Read More</a>
  </div>
  <div class="service-card" style="left:363px;top:2509px">
    <div class="service-icon"><svg width="40" height="40" viewBox="0 0 40 40" fill="none" stroke="#333" stroke-width="1.6"><path d="M4 34L17 14l6 9 4-5 9 16z M20 18V6 M20 6h9l-2 3 2 3h-9"/></svg></div>
    <div class="service-title">Excepteursi Ntaccae</div>
    <p class="service-text">Perspiciatis unde omnis iste natus error sit volu ptatem accusa ntium dolor emque laudan tiumsequi</p>
    <a class="service-link">Read More</a>
  </div>
  <div class="service-card" style="left:614px;top:2509px">
    <div class="service-icon"><svg width="40" height="40" viewBox="0 0 40 40" fill="none" stroke="#333" stroke-width="1.6"><rect x="6" y="8" width="26" height="20" rx="2"/><path d="M11 23v-5 M16 23v-9 M21 23v-7 M14 32h10"/><circle cx="29" cy="26" r="5"/><path d="M33 30l4 4"/></svg></div>
    <div class="service-title">Voluptem accusant</div>
    <p class="service-text">Perspiciatis unde omnis iste natus error sit volu ptatem accusa ntium dolor emque laudan tiumsequi</p>
    <a class="service-link">Read More</a>
  </div>
  <div class="service-card" style="left:866px;top:2509px">
    <div class="service-icon"><svg width="40" height="40" viewBox="0 0 40 40" fill="none" stroke="#333" stroke-width="1.6"><circle cx="20" cy="20" r="5"/><circle cx="20" cy="7" r="3"/><circle cx="20" cy="33" r="3"/><circle cx="7" cy="20" r="3"/><circle cx="33" cy="20" r="3"/><path d="M20 10v5 M20 25v5 M10 20h5 M25 20h5"/></svg></div>
    <div class="service-title">Nemoen Imipsam</div>
    <p class="service-text">Perspiciatis unde omnis iste natus error sit volu ptatem accusa ntium dolor emque laudan tiumsequi</p>
    <a class="service-link">Read More</a>
  </div>
</section>

<!-- ===== Contact ===== -->
<section id="contact">
  <h2 class="section-title" style="top:3022px">Contact <span>Us</span></h2>
  <p class="contact-text">Perspiciatis unde omnis iste natus error sit voluptatem accusantium doloremque laudantium, totam rem aperiam.</p>
  <div class="field" style="left:247px;top:3157px;width:341px;height:44px">Full Name*</div>
  <div class="field" style="left:611px;top:3157px;width:341px;height:44px">Email*</div>
  <div class="field" style="left:247px;top:3219px;width:341px;height:44px">Phone*</div>
  <div class="field" style="left:611px;top:3219px;width:341px;height:44px">Company*</div>
  <div class="field" style="left:247px;top:3281px;width:705px;height:149px">Message*</div>
  <a class="btn" style="left:543px;top:3457px;width:115px;height:34px">SUBMIT</a>
</section>

<!-- ===== Footer ===== -->
<footer>
  <svg class="abs" style="left:0;top:3590px" width="1200" height="512" viewBox="0 0 1200 512">
    <path d="M0 170C120 40 400 10 700 20C900 28 1080 70 1200 110V512H0Z" fill="var(--teal)"/>
    <path d="M0 175C150 60 420 40 700 45C900 50 1080 90 1200 130V512H0Z" fill="var(--navy)"/>
  </svg>

  <div class="footer-brand">
    <div class="brand-name">VALRO</div>
    <div class="brand-sub">VALLEY APPRAISAL AND RESOLUTION OFFICE</div>
  </div>
  <div class="social" style="left:155px"></div>
  <div class="social" style="left:217px"></div>
  <div class="social" style="left:279px"></div>

  <h3 class="footer-head" style="left:457px">QUICK LINKS</h3>
  <ul class="footer-links" style="left:457px">
    <li>Home</li><li>About Us</li><li>What we do</li><li>How we work</li><li>Client</li><li>Blog</li>
  </ul>
  <h3 class="footer-head" style="left:668px">LINKS</h3>
  <ul class="footer-links" style="left:668px">
    <li>My Account</li><li>Team</li><li>About Us</li><li>Careers</li><li>Our Values</li>
  </ul>

  <h3 class="footer-head" style="left:854px">CONTACT US</h3>
  <div class="contact-icon" style="top:3826px">
    <svg width="16" height="16" viewBox="0 0 16 16"><path d="M8 1a5 5 0 0 0-5 5c0 4 5 9 5 9s5-5 5-9a5 5 0 0 0-5-5z" fill="#fff"/><circle cx="8" cy="6" r="2" fill="var(--navy)"/></svg>
  </div>
  <p class="contact-line" style="top:3822px">14 Harbor Mill Lane, Easton,<br>Ohio, 43001, USA</p>
  <div class="contact-icon" style="top:3892px">
    <svg width="16" height="16" viewBox="0 0 16 16"><rect x="2" y="4" width="12" height="8" rx="1" fill="#fff"/><path d="M2 4l6 5 6-5" fill="none" stroke="var(--navy)" stroke-width="1.2"/></svg>
  </div>
  <p class="contact-line" style="top:3897px">hello@valroclaims.example</p>
  <div class="contact-icon" style="top:3948px">
    <svg width="16" height="16" viewBox="0 0 16 16"><path d="M4 2l2 3-1.5 1.5a8 8 0 0 0 5 5L11 10l3 2-1 2.5C7 14 2 9 1.5 3z" fill="#fff"/></svg>
  </div>
  <p class="contact-line" style="top:3953px">555 010 2468</p>

  <div class="to-top">
    <svg width="16" height="16" viewBox="0 0 16 16"><path d="M4 10l4-4 4 4" fill="none" stroke="#fff" stroke-width="2"/></svg>
  </div>

  <div class="footer-rule"></div>
  <p class="footer-bottom" style="left:111px">Copyrights © 2021 | All Rights Reserved.</p>
  <p class="footer-bottom" style="left:854px">Privacy Policy</p>
  <p class="footer-bottom" style="left:972px">|</p>
  <p class="footer-bottom" style="left:1010px">Terms of use</p>
</footer>

</body>
</html>
```